Email marketing template

Job type:
Email marketing

Task description:
We would like to send an E-card to our clients wishing them a Merry Christmas

Copy for email marketing:

Seasons Greetings from everyone at RLT…

This year we are supporting our chosen charities by making a donation to help them continue their hard work making a difference. Have a look at our website to find more about the chosen charities we are supporting this Christmas:

http://www.roslyntarbet.example/Our-Approach/Brightfield

Best wishes,

The RLT team

Logo text:
RLT

Descriptive words:
Fun
Playful
Bold
Festive

Deadline:
Monday 16th December

Other information:
We will require you to provide us with HTML coding and uploading to Post Wren. We will then process payment upon testing final materials.

Industry/Entity Type

Marketing

```html
<!DOCTYPE html>
<html lang="en">
<head>
<meta charset="utf-8">
<title>Seasons Greetings from everyone at RLT</title>
<link rel="stylesheet" href="https://fonts.googleapis.com/css2?family=Damion&family=Quicksand:wght@400;600&display=swap">
<style>
  :root {
    --night-top: #0b1424;
    --night-mid: #16243a;
    --pine-dark: #1c2b26;
    --snow-glow: #c9d6ea;
    --snow-light: #e9eef7;
    --lights-warm: #f3c77a;
    --title-white: #ffffff;
    --tagline-teal: #7fd6e4;
    --badge-white: #ffffff;
    --brand-ink: #3a3f4a;
    --brand-accent: #6f8fd8;
  }
  * { margin: 0; padding: 0; box-sizing: border-box; }
  html, body {
    width: 1200px;
    height: 508px;
    overflow: hidden;
    background: var(--night-top);
  }
  .ecard {
    position: relative;
    width: 1200px;
    height: 508px;
    overflow: hidden;
  }
  .ecard__scene {
    position: absolute;
    inset: 0;
    background:
      radial-gradient(ellipse 260px 300px at 250px 300px, rgba(243, 199, 122, 0.45), rgba(243, 199, 122, 0) 70%),
      radial-gradient(ellipse 900px 140px at 400px 520px, var(--snow-light), rgba(201, 214, 234, 0) 75%),
      linear-gradient(180deg, var(--night-top) 0%, var(--pine-dark) 45%, var(--night-mid) 72%, var(--snow-glow) 100%);
  }
  .ecard__title {
    position: absolute;
    left: 560px;
    top: 30px;
    width: 600px;
    font-family: "Damion", cursive;
    font-weight: 400;
    color: var(--title-white);
    line-height: 0.95;
  }
  .ecard__title-line {
    display: block;
    font-size: 150px;
  }
  .ecard__title-line--first { padding-left: 90px; }
  .ecard__title-line--second { margin-top: -18px; }
  .ecard__tagline {
    position: absolute;
    left: 612px;
    top: 292px;
    font-family: "Quicksand", sans-serif;
    font-weight: 400;
    font-size: 38px;
    letter-spacing: 1px;
    color: var(--tagline-teal);
    white-space: nowrap;
  }
  .ecard__badge {
    position: absolute;
    left: 600px;
    top: 336px;
    width: 408px;
    height: 156px;
    background: var(--badge-white);
    display: flex;
    align-items: center;
    justify-content: center;
    gap: 26px;
  }
  .ecard__badge-mark {
    width: 56px;
    height: 56px;
    background: var(--brand-accent);
  }
  .ecard__badge-name {
    font-family: "Quicksand", sans-serif;
    font-weight: 600;
    font-size: 96px;
    line-height: 1;
    color: var(--brand-ink);
  }
</style>
</head>
<body>
  <main class="ecard">
    <div class="ecard__scene" role="img" aria-label="Photograph of a snow-covered fir tree strung with coloured Christmas lights in a snowy forest at night"></div>

    <h1 class="ecard__title">
      <span class="ecard__title-line ecard__title-line--first">Seasons</span>
      <span class="ecard__title-line ecard__title-line--second">Greetings</span>
    </h1>

    <p class="ecard__tagline">from everyone at</p>

    <div class="ecard__badge">
      <span class="ecard__badge-mark" aria-hidden="true"></span>
      <span class="ecard__badge-name">RLT</span>
    </div>
  </main>
</body>
</html>
```